Hdmi 4K solution Hidden cable solution for wall hung TV, Flyer

VELNAR is an audio visual company that install cabling into new construction of homes.

Design Objective:
Design a 1-Page flyer on a dark background that needs to represent today's latest picture quality and sound solution. This flyer will be in a take home pack with all other components of a new home build (like, bathrooms, paint colour, carpets, flooring, window furnishing ETC) for clients to choose in the design process of building a new home

- I would like this to look as professional as possible and to stand out once clients Turn to our HDMI flyer.

Would like to see the following CONTENTS on the flyer:
- 4k symbol plus VELNAR logo
- "Plimz" brand Logo voted best quality by intergation experts 2015-16-17-18
- image of a TV mounted on a wall representing a wall hung TV with a line diagram behind it (like seeing through the wall) indicating the cable behind the wall (Tavlite,dry wall )
- photo attached of a sample input

- Automated, Easy
- No clutter or dangling cables on the wall
- 4k guarantee

- Clean, hidden cables. Easy,
- Fully Tested and ready to go
- Just Plug in and way go DIY When you move in to your home
-Product is used in the following rooms:
* Home theatre
* Dining / living room
* Fire place
* Alfresco cabana
* Pool house
* Office

"Choosing the right HDMI Cable to prewire hasn't been easier"

Aesthetics or Preferred Style:
Looking for life style Sound lounge feel in the flyer (please check attached sample brochure and flyer)

Logo is supplied and would like to keep it somewhere in the flyer please. It has sentimental significance.

Actual photo attached of the product ( HDMI) Input and output)

Target Market(s)

New home buyers upgrading accessories in design studios. This product need to be easily identified as inexperienced sales people are usually selling these in display studios. Represent today's latest version of HDMI and fun clear defining tones/colors and picture. Looking for elegant and professional colours /aesthetics

Font styles to use
Other font styles liked:
• see attachments

Requirements
Must have
• This flyer will be in a take home pack with all other components of a new home build ex. bathrooms, paint colour, carpets, flooring, window furnishing ETC for clients to choose in the design process of building a new home.
• I would like this to look as professional as possible and to stand out once clients Turn to our HDMI flyer.
Nice to have
• Elegant feel with dark tones to help bridge the professional finish we do from day to day on site on new homes.
• Easy to read ond captivating to choose the HDMI solution to be installed into the new home
Should not have
• I am happy to try something new and not pedestrian or similar to other people as we have pioneered this type of installation package.

```html
<!DOCTYPE html>
<html lang="en">
<head>
<meta charset="utf-8">
<title>VELNAR – Our Service Flyer</title>
<link href="https://fonts.googleapis.com/css2?family=Montserrat:wght@600;700;800&family=Questrial&display=swap" rel="stylesheet">
<style>
  :root {
    --canvas: #d6d6d8;
    --navy: #1f418d;
    --navy-deep: #183677;
    --royal: #2c57a8;
    --sky: #1e9ad8;
    --sky-light: #3fb2ea;
    --white: #ffffff;
    --ink: #3a3d44;
    --ink-soft: #6b6f78;
  }
  * { box-sizing: border-box; margin: 0; padding: 0; }
  html, body { width: 1200px; height: 1200px; overflow: hidden; }
  body {
    background: var(--canvas);
    font-family: "Questrial", "Century Gothic", sans-serif;
    color: var(--ink);
    position: relative;
  }
  .flyer {
    position: absolute; left: 197px; top: 30px;
    width: 806px; height: 1140px;
    background: linear-gradient(180deg, var(--royal) 0%, var(--navy) 60%, var(--navy-deep) 100%);
    overflow: hidden;
  }
  .logo-panel {
    position: absolute; left: 21px; top: 22px; width: 336px; height: 234px;
    background: var(--white);
    display: flex; flex-direction: column; align-items: center; justify-content: center; gap: 6px;
  }
  .brand-row { display: flex; align-items: center; gap: 12px; }
  .brand-dot { width: 22px; height: 22px; border-radius: 50%; background: var(--sky); }
  .brand-name {
    font-family: "Montserrat", sans-serif; font-weight: 700;
    font-size: 44px; letter-spacing: 1px; color: var(--ink);
  }
  .brand-tag { font-size: 10px; letter-spacing: 1px; color: var(--ink-soft); }
  .photo { position: absolute; border: 2px solid var(--sky-light); }
  .photo-shelving { left: 366px; top: 22px; width: 202px; height: 234px;
    background: linear-gradient(180deg, #d9cbb6 0%, #c3a27c 55%, #efece7 100%); }
  .photo-lounge { left: 577px; top: 22px; width: 207px; height: 234px;
    background: linear-gradient(180deg, #efedea 0%, #55614f 35%, #222125 70%, #e8e5e0 100%); }
  .photo-media-wall { left: 22px; top: 270px; width: 249px; height: 237px;
    background: linear-gradient(180deg, #ecebe8 0%, #d7c3a9 40%, #f3f2ef 100%); }
  .photo-cabinetry { left: 280px; top: 270px; width: 247px; height: 237px;
    background: linear-gradient(180deg, #e3d6c2 0%, #5a7897 30%, #c89c6d 70%, #93694a 100%); }
  .photo-feature-wall { left: 536px; top: 270px; width: 248px; height: 237px;
    background: linear-gradient(180deg, #f6f4f0 0%, #3a3c42 40%, #f3f0ec 75%, #e9e4dd 100%); }
  .badge {
    position: absolute; width: 70px; height: 70px; border-radius: 50%;
    background: var(--sky); border: 3px solid var(--white);
    display: flex; align-items: center; justify-content: center;
  }
  .badge-sound { left: 544px; top: 106px; }
  .badge-screen { left: 235px; top: 355px; }
  .badge-light { left: 501px; top: 355px; }
  .headline {
    position: absolute; left: 0; right: 0; top: 520px;
    text-align: center; color: var(--white);
    font-family: "Montserrat", sans-serif; font-weight: 700; font-size: 64px; letter-spacing: 1px;
  }
  .content-panel {
    position: absolute; left: 23px; top: 612px; width: 758px; height: 406px;
    background: var(--white);
  }
  .bullets { position: absolute; top: 36px; list-style: none; font-size: 19.5px; line-height: 25px; }
  .bullets li { position: relative; padding-left: 20px; }
  .bullets li::before {
    content: ""; position: absolute; left: 0; top: 8px; width: 11px; height: 11px;
    border-radius: 50%; background: var(--sky);
  }
  .bullets-left { left: 14px; width: 335px; }
  .bullets-right { left: 394px; width: 345px; }
  .divider { position: absolute; left: 375px; top: 38px; width: 2px; height: 80px; background: var(--sky); }
  .products { position: absolute; left: 0; top: 160px; width: 758px; height: 246px; }
  .rooms-title {
    position: absolute; left: 0; right: 0; top: 303px; text-align: center;
    color: var(--sky); font-family: "Montserrat", sans-serif; font-weight: 600; font-size: 19px;
  }
  .rooms {
    position: absolute; left: 40px; right: 40px; top: 335px;
    text-align: center; font-size: 19.5px; line-height: 25px;
  }
  .rooms span { white-space: nowrap; }
  .rooms .tick {
    display: inline-block; width: 11px; height: 11px; border-radius: 50%;
    background: var(--sky); margin: 0 6px 1px 12px; vertical-align: middle;
  }
  .quote {
    position: absolute; left: 0; right: 0; top: 1034px;
    color: var(--white); font-family: "Montserrat", sans-serif; font-weight: 700;
    font-size: 28px; line-height: 36px; text-align: center;
  }
  .quote .mark { font-size: 48px; font-weight: 800; vertical-align: -12px; }
</style>
</head>
<body>
<main class="flyer">
  <div class="logo-panel">
    <div class="brand-row">
      <span class="brand-dot"></span>
      <span class="brand-name">VELNAR</span>
    </div>
    <span class="brand-tag">AUDIO-VISUAL CONTRACTORS</span>
  </div>

  <div class="photo photo-shelving" role="img" aria-label="Living room with wall-mounted TV set into timber shelving"></div>
  <div class="photo photo-lounge" role="img" aria-label="Lounge with TV showing a landscape above a dark cabinet and flowers"></div>
  <div class="photo photo-media-wall" role="img" aria-label="White media wall with TV, soundbar and pendant lights"></div>
  <div class="photo photo-cabinetry" role="img" aria-label="TV above timber cabinetry in a warm-lit family room"></div>
  <div class="photo photo-feature-wall" role="img" aria-label="Wall-hung TV above white cabinets and floating shelves"></div>

  <div class="badge badge-sound">
    <svg width="40" height="34" viewBox="0 0 40 34" fill="none" stroke="#fff" stroke-width="3" stroke-linecap="round">
      <path d="M3 12h7l9-8v26l-9-8H3z" fill="#fff"/>
      <path d="M25 11c3 3 3 9 0 12M29 7c5 5 5 15 0 20M33 3c7 7 7 21 0 28"/>
    </svg>
  </div>
  <div class="badge badge-screen">
    <svg width="38" height="34" viewBox="0 0 38 34" fill="none" stroke="#fff" stroke-width="3.5">
      <rect x="3" y="3" width="32" height="22" rx="2"/>
      <path d="M19 25v5M11 31h16" stroke-linecap="round"/>
    </svg>
  </div>
  <div class="badge badge-light">
    <svg width="40" height="40" viewBox="0 0 40 40" fill="none" stroke="#fff" stroke-width="3.5" stroke-linecap="round">
      <circle cx="20" cy="20" r="5"/>
      <path d="M20 3v5M20 32v5M3 20h5M32 20h5M8 8l3.5 3.5M28.5 28.5L32 32M8 32l3.5-3.5M28.5 11.5L32 8"/>
    </svg>
  </div>

  <h1 class="headline">OUR SERVICE</h1>

  <section class="content-panel">
    <ul class="bullets bullets-left">
      <li>Automated, Easy</li>
      <li>No clutter or dangling cables on the wall</li>
      <li>4k guarantee</li>
    </ul>
    <div class="divider"></div>
    <ul class="bullets bullets-right">
      <li>Clean, hidden cables. Easy,</li>
      <li>Fully Tested and ready to go</li>
      <li>Just Plug in and way go DIY When you move in to your home</li>
    </ul>

    <svg class="products" viewBox="0 0 758 246">
      <path d="M2 246V65H40M730 65H756V246" fill="none" stroke="#1f418d" stroke-width="3"/>
      <polygon points="40,4 244,4 228,130 40,130" fill="#fff" stroke="#1f418d" stroke-width="3"/>
      <polygon points="50,14 232,14 219,120 50,120" fill="#6b6a5c" role="img" aria-label="Braided HDMI cable with gold connector"/>
      <polygon points="254,4 492,4 476,130 237,130" fill="#fff" stroke="#1f418d" stroke-width="3"/>
      <polygon points="263,14 480,14 467,120 248,120" fill="#2b2b2e" role="img" aria-label="Pair of Plimz HDMI plugs"/>
      <polygon points="501,4 730,4 730,130 485,130" fill="#fff" stroke="#1f418d" stroke-width="3"/>
      <rect x="540" y="22" width="160" height="88" rx="8" fill="#ece7dc" role="img" aria-label="White HDMI wall plate"/>
    </svg>

    <div class="rooms-title">Product is used in the following rooms:</div>
    <div class="rooms">
      <span><span class="tick" style="margin-left:0"></span>Home theatre</span>
      <span><span class="tick"></span>Dining / living room</span>
      <span><span class="tick"></span>Fire place</span>
      <span><span class="tick"></span>Alfresco</span><br>
      <span>cabana</span>
      <span><span class="tick"></span>Pool house</span>
      <span><span class="tick"></span>Office</span>
    </div>
  </section>

  <p class="quote"><span class="mark">“</span> Choosing the right HDMI Cable to<br>prewire hasn't been easier <span class="mark">”</span></p>
</main>
</body>
</html>
```